Web Site Design

We need to design the whole web site for our small start up. We sell hospitality and culinary art internships abroad. I did my own design with WIX which is horrible meanwhile I started with my business. You can see it www.brindle-passage.org I will need you to create a new and attractive web site and to leave it working on wix. The internship destinations are United Arab Emirates, Thailand, China, Spain, Brazil and maybe leave a couple of pages for future destinations.You could also get other ideas of other sites that do internships.

Target Market(s)

Students and recent graduates of hospitality and culinary art majors

Industry/Entity Type

Education

Number of Pages Required

5+ page

Requirements
Must have
• Addittional to our program destinations, or to the pages in the current site. The website must contain a page for Universities or Hotels who require our service

```html
<!DOCTYPE html>
<html lang="en">
<head>
<meta charset="utf-8">
<title>Brindle Passage – Hospitality Internship Program</title>
<link rel="stylesheet" href="https://fonts.googleapis.com/css2?family=Chivo:wght@400;700;900&family=Lato:wght@400;700&display=swap">
<style>
  :root {
    --teal: #4f8f93;
    --teal-dark: #3d6e70;
    --teal-light: #5aa3a6;
    --ink: #111;
    --white: #fff;
    --contact-bg: #cddcdc;
    --footer-bg: #ececec;
    --footer-text: #666;
    --hero-a: #0b1716;
    --hero-b: #1d4440;
  }
  * { box-sizing: border-box; margin: 0; padding: 0; }
  html, body { width: 1200px; height: 2490px; overflow: hidden; }
  body { position: relative; background: var(--white); font-family: "Chivo", Arial, sans-serif; color: var(--ink); }
  .abs { position: absolute; }
  .center { left: 0; width: 1200px; text-align: center; }

  /* hero */
  .hero { top: 0; left: 0; width: 1200px; height: 526px; overflow: hidden; }
  .hero-photo { position: absolute; inset: 0;
    background: radial-gradient(ellipse 60% 70% at 60% 35%, #2f5a55 0%, rgba(22,52,48,.9) 45%, transparent 80%),
                linear-gradient(180deg, #000 0%, var(--hero-a) 20%, var(--hero-b) 70%, #173a37 100%); }
  .brand { position: absolute; left: 133px; top: 13px; display: flex; align-items: center; gap: 14px; }
  .brand-mark { width: 86px; height: 86px; border-radius: 50%; border: 3px solid var(--white); }
  .brand-name { color: var(--white); font-family: "Chivo", Arial, sans-serif; font-size: 20px; line-height: 1.1; width: 110px; }
  .nav { position: absolute; left: 511px; top: 45px; display: flex; gap: 22px; font-size: 17px; }
  .nav a { color: var(--white); text-decoration: none; }
  .nav a.is-active { color: var(--teal-light); }
  .hero-title { position: absolute; left: 133px; top: 340px; line-height: 1; }
  .hero-title .kicker { display: block; color: var(--teal); font-weight: 900; font-size: 46px; letter-spacing: 1px; }
  .hero-title .main { display: block; color: var(--white); font-size: 46px; letter-spacing: 1px; margin-top: 2px; }
  .btn { display: inline-block; background: var(--teal); color: var(--white); font-size: 21px; text-align: center; text-decoration: none; line-height: 50px; height: 50px; }
  .hero-btn { position: absolute; left: 697px; top: 377px; width: 163px; }
  .dots { position: absolute; top: 478px; left: 560px; display: flex; gap: 17px; }
  .dots span { width: 16px; height: 16px; border-radius: 50%; background: var(--white); }
  .dots span.is-current { background: var(--teal); }

  .curve-shadow { position: absolute; left: 100px; width: 1000px; height: 40px;
    background: radial-gradient(ellipse 50% 100% at 50% 0%, rgba(0,0,0,.28), rgba(0,0,0,0) 70%); }

  h2 { font-weight: 400; letter-spacing: 1px; }
  .section-text { font-size: 21px; line-height: 26px; width: 940px; margin: 0 auto; }

  /* welcome */
  .welcome-title { top: 588px; font-size: 43px; }
  .welcome-title em { font-style: normal; color: var(--teal); }
  .welcome-text { top: 658px; }
  .welcome-btn { position: absolute; left: 521px; top: 798px; width: 163px; background: var(--teal-dark); box-shadow: 0 6px 10px rgba(0,0,0,.35); }

  /* about */
  .about { top: 868px; left: 0; width: 1200px; height: 326px;
    background: radial-gradient(ellipse 40% 80% at 75% 40%, #2a4644 0%, transparent 70%),
                linear-gradient(180deg, #0d1616 0%, #182726 60%, #0f1a19 100%); }
  .about-title { top: 903px; font-size: 43px; color: var(--white); }
  .about-text { top: 972px; color: var(--white); }
  .about-btn { position: absolute; left: 521px; top: 1110px; width: 163px; }

  /* destinations */
  .dest-title { top: 1248px; font-size: 46px; letter-spacing: 3px; }
  .dest { position: absolute; top: 1348px; width: 220px; text-align: center; }
  .dest-map { height: 150px; margin: 0 auto; background: radial-gradient(ellipse at 50% 50%, var(--teal) 0%, var(--teal) 55%, rgba(79,143,147,0) 72%); }
  .dest-name { display: block; margin-top: 28px; font-size: 31px; letter-spacing: 3px; }

  /* contact */
  .contact { top: 1590px; left: 0; width: 1200px; height: 551px; background: var(--contact-bg); }
  .contact-title { top: 1632px; font-size: 46px; letter-spacing: 2px; }
  .field { position: absolute; left: 136px; width: 370px; height: 50px; border: 3px solid var(--teal); border-radius: 7px; padding: 9px 18px; font-size: 25px; color: var(--teal); background: transparent; }
  .field.is-focus { background: var(--teal); color: var(--white); }
  .field.message { height: 145px; }
  .pitch { position: absolute; left: 603px; top: 1730px; width: 500px; }
  .pitch h3 { font-weight: 400; font-size: 31px; line-height: 36px; letter-spacing: 2px; width: 400px; }
  .pitch p { margin-top: 24px; font-size: 21px; line-height: 35px; letter-spacing: 1px; }
  .send-btn { position: absolute; left: 603px; top: 2040px; width: 162px; font-size: 22px; }

  /* footer */
  .footer { top: 2163px; left: 0; width: 1200px; height: 327px; background: var(--footer-bg); font-family: "Lato", Arial, sans-serif; font-size: 12.5px; color: var(--footer-text); }
  .footer-col { position: absolute; top: 62px; line-height: 22.4px; }
  .footer-col h4 { font-size: 12.5px; font-weight: 700; color: #333; margin-bottom: 4px; }
  .footer-col ul { list-style: none; }
  .footer-col .is-strong { color: #111; font-weight: 700; }
  .footer-col .mail { color: var(--teal); font-weight: 700; }
  .copyright { position: absolute; left: 137px; top: 250px; color: #555; }
  .copyright b { color: #111; font-weight: 400; }
  .social { position: absolute; left: 755px; top: 236px; width: 316px; display: flex; align-items: center; gap: 16px; padding-bottom: 14px; border-bottom: 1px solid #cfcfcf; color: #555; }
  .social a { color: var(--teal); text-decoration: none; display: flex; align-items: center; gap: 6px; }
  .social .dot { width: 12px; height: 12px; background: var(--teal); border-radius: 2px; }
</style>
</head>
<body>

<header class="abs hero">
  <div class="hero-photo" role="img" aria-label="Photo of a surgical team at work in an operating room, dark teal tones"></div>
  <div class="brand">
    <span class="brand-mark"></span>
    <span class="brand-name">Brindle Passage</span>
  </div>
  <nav class="nav">
    <a class="is-active" href="#">Home</a>
    <a href="#">About Us</a>
    <a href="#">Destinations</a>
    <a href="#">Hospitals &amp; University</a>
    <a href="#">Contact</a>
  </nav>
  <h1 class="hero-title"><span class="kicker">HOSPITALITY</span><span class="main">INTERNSHIP PROGRAM</span></h1>
  <a class="btn hero-btn" href="#">Learn More</a>
  <div class="dots"><span></span><span></span><span class="is-current"></span></div>
</header>
<div class="curve-shadow" style="top:526px"></div>

<section>
  <h2 class="abs center welcome-title">WELCOME TO <em>BRINDLEPASSAGE.ORG</em></h2>
  <p class="abs center welcome-text"><span class="section-text" style="display:block">Lorem Ipsum is simply dummy text of the printing and typesetting industry. Lorem Ipsum has been the industry's standard dummy text ever since the 1500s, when an unknown printer took a galley of type and scrambled it to make a type specimen book. It has survived not only five centuries,Lorem Ipsum is simply dummy text of the pri</span></p>
  <a class="btn welcome-btn" href="#">Learn More</a>
</section>

<section>
  <div class="abs about" role="img" aria-label="Darkened photo of surgeons in an operating theatre"></div>
  <h2 class="abs center about-title">ABOUT US</h2>
  <p class="abs center about-text"><span class="section-text" style="display:block">Lorem Ipsum is simply dummy text of the printing and typesetting industry. Lorem Ipsum has been the industry's standard dummy text ever since the 1500s, when an unknown printer took a galley of type and scrambled it to make a type specimen book. It has survived not only five centuries,Lorem Ipsum is simply dummy text of the pri</span></p>
  <a class="btn about-btn" href="#">Learn More</a>
</section>
<div class="curve-shadow" style="top:1194px"></div>

<section>
  <h2 class="abs center dest-title">DESTINATIONS</h2>
  <div class="dest" style="left:232px"><div class="dest-map" role="img" aria-label="Teal map of China" style="width:210px"></div><span class="dest-name">CHINA</span></div>
  <div class="dest" style="left:511px"><div class="dest-map" role="img" aria-label="Teal map of Spain" style="width:190px"></div><span class="dest-name">SPAIN</span></div>
  <div class="dest" style="left:781px"><div class="dest-map" role="img" aria-label="Teal map of France" style="width:140px"></div><span class="dest-name">FRANCE</span></div>
</section>

<section>
  <div class="abs contact"></div>
  <div class="curve-shadow" style="top:1590px"></div>
  <h2 class="abs center contact-title">CONTACT US</h2>
  <div class="field is-focus" style="top:1708px">Number</div>
  <div class="field" style="top:1788px">Email</div>
  <div class="field" style="top:1868px">Affair</div>
  <div class="field message" style="top:1947px">Message</div>
  <div class="pitch">
    <h3>MAKE YOUR RESUME STAND OUT WITH AN INTERNATIONAL EXPERIENCE</h3>
    <p>HOSPITALITY INTERNSHIPS ARE OUR SPE-<br>CIALTY! TAKE YOUR PAID INTERNSHIP IN ONE<br>OF OUR TOP INTERNATIONAL FIVE-STAR<br>HOTELS</p>
  </div>
  <a class="btn send-btn" href="#">Send</a>
</section>
<div class="curve-shadow" style="top:2141px"></div>

<footer class="abs footer">
  <div class="footer-col" style="left:134px">
    <h4>CONTACT US AT:</h4>
    <ul><li>Your addres here</li><li>Phone: (+1) 123 456 789</li><li>Email: <span class="mail">hello@brindlepassage.org</span></li></ul>
  </div>
  <div class="footer-col" style="left:435px">
    <h4>ABOUT US:</h4>
    <ul><li>Our History</li><li>Our Clients</li><li>Partners</li><li>Meet the Team</li></ul>
  </div>
  <div class="footer-col" style="left:613px">
    <h4>SERVICES:</h4>
    <ul><li>Hospitals &amp; Universities</li><li class="is-strong">2nd service</li><li>3rd service</li><li>4th service</li><li>5th service</li></ul>
  </div>
  <div class="footer-col" style="left:787px">
    <h4>CASE STUDIES:</h4>
    <ul><li>Medical Malpraxis</li><li>DUI cases</li><li>Mediation cases</li><li>Family care</li><li>Others</li></ul>
  </div>
  <div class="footer-col" style="left:966px">
    <h4>CAREERS:</h4>
    <ul><li>Available Jobs</li><li>Internship</li><li>Send your Resume</li></ul>
  </div>
  <p class="copyright">copyright 2018 - <b>Brindle Passage.org</b></p>
  <div class="social">
    <span>Follow us on:</span>
    <a href="#"><span class="dot"></span>Facepage</a>
    <a href="#"><span class="dot"></span>Chirper</a>
    <a href="#"><svg width="13" height="13" viewBox="0 0 13 13" aria-hidden="true"><circle cx="2" cy="11" r="2" fill="#4f8f93"/><path d="M0 5a8 8 0 0 1 8 8M0 1a12 12 0 0 1 12 12" stroke="#4f8f93" stroke-width="2" fill="none"/></svg>RSS</a>
  </div>
</footer>

</body>
</html>
```